Brightwater Dental
Stationary for Pediatric Dental & Orthodontics - Health
Stationary for Pediatric Dental & Orthodontics
Bright & Fun-filled
Pediatrics & Orthodontics
Larkspur Hollow Prof. Center 48517 Larkspur Hollow Ave. Suite B-07 Gaithersburg, MD 20886
info@brightwaterdental.org
www.brightwaterdental.org
I have uploaded the co logo to use for the card. I am looking for biz card (2 sided), appointment card, rewards biz card (can explain later, but basically the biz card with an offer on the back), referral pad, envelope (1 sided-no flap work), letterhead, & folder. I would also like to have a QR code linked to the company website on all materials, if it can be color and still work that would be great. I uploaded the static code that I have currently.
This only needs to be on the back of the biz card not the other materials........... Helping Children Who Need: Fillings, Braces, Crowns, Laughing Gas, Whitening, Mouthguards, Hospital Care, Special Needs Care, Clearvane, Nightguards, Cosmetics, Extractions, Walk-in Emergencies, Dental Home.................... Carewell and Most Insurances Accepted

```html
<!DOCTYPE html>
<html lang="en">
<head>
<meta charset="utf-8">
<title>Brightwater Dental – Business Card</title>
<link rel="stylesheet" href="https://fonts.googleapis.com/css2?family=Open+Sans:wght@400;600&display=swap">
<style>
  :root {
    --bg: #d9dadb;
    --card: #ffffff;
    --blue: #2d67c4;
    --blue-dark: #1f4f9e;
    --green: #7cc242;
    --ink: #3a3f47;
    --muted: #5a6068;
  }
  * { margin: 0; padding: 0; box-sizing: border-box; }
  html, body { width: 1200px; height: 895px; overflow: hidden; }
  body {
    background: var(--bg);
    font-family: "Open Sans", Arial, sans-serif;
    color: var(--ink);
    position: relative;
  }
  .card {
    position: absolute;
    left: 250px;
    width: 700px;
    height: 400px;
    background: var(--card);
    overflow: hidden;
  }
  .card--back { top: 30px; }
  .card--front { top: 465px; }

  .frame {
    position: absolute;
    left: 26px; top: 26px; right: 26px; bottom: 26px;
    border: 2px solid var(--green);
  }
  .brand {
    position: absolute;
    display: flex;
    align-items: center;
    gap: 12px;
    color: var(--blue);
    font-weight: 600;
  }
  .brand__mark {
    width: 26px; height: 26px;
    background: var(--green);
  }
  .card--back .brand {
    left: 0; right: 0; top: 98px;
    justify-content: center;
    font-size: 38px;
  }
  .back-band {
    position: absolute;
    left: 0; right: 0; bottom: 50px;
    height: 96px;
    background: var(--blue);
    display: flex; align-items: center; justify-content: center;
  }
  .back-band__url {
    color: #fff;
    font-size: 26px;
    letter-spacing: 1px;
  }

  .card--front .brand {
    left: 60px; top: 62px;
    font-size: 28px;
  }
  .front-band {
    position: absolute;
    left: 0; right: 0; bottom: 0;
    height: 44px;
    background: var(--blue);
  }
  .front-accent {
    position: absolute;
    left: 0; bottom: 44px;
    width: 70px; height: 16px;
    background: var(--green);
  }
  .front-side {
    position: absolute;
    left: 0; top: 166px; bottom: 44px;
    width: 70px;
    background: var(--blue);
    clip-path: polygon(0 0, 100% 40%, 100% 100%, 0 100%);
    opacity: 0;
  }
  .contact {
    position: absolute;
    display: flex; align-items: center; gap: 12px;
    font-size: 15px;
    color: var(--muted);
  }
  .contact svg { width: 20px; height: 20px; flex: none; }
  .contact--phone { left: 60px; top: 150px; }
  .contact--email { left: 60px; top: 184px; }
  .person {
    position: absolute;
    right: 70px; top: 150px;
    text-align: right;
  }
  .person__name { color: var(--blue); font-size: 22px; font-weight: 400; }
  .person__role { font-size: 16px; color: var(--ink); }
  .contact--addr { left: 360px; top: 252px; align-items: flex-start; line-height: 1.4; }
  .contact--web { left: 360px; top: 306px; }
</style>
</head>
<body>

<section class="card card--back" aria-label="Business card back">
  <div class="frame"></div>
  <div class="brand"><span class="brand__mark"></span><span>Brightwater Dental</span></div>
  <div class="back-band"><span class="back-band__url">www.brightwaterdental.org</span></div>
</section>

<section class="card card--front" aria-label="Business card front">
  <div class="frame"></div>
  <div class="front-accent"></div>
  <div class="front-band"></div>
  <div class="brand"><span class="brand__mark"></span><span>Brightwater Dental</span></div>

  <div class="contact contact--phone">
    <svg viewBox="0 0 20 20"><rect width="20" height="20" rx="3" fill="var(--blue)"/><path d="M7 5l2 3-1.3 1.3a7 7 0 0 0 3 3L12 11l3 2-1 2c-4 0-9-5-9-9z" fill="#fff"/></svg>
    <span>014 762 3058</span>
  </div>
  <div class="contact contact--email">
    <svg viewBox="0 0 20 20"><rect width="20" height="20" rx="3" fill="var(--blue)"/><rect x="4" y="6" width="12" height="8" fill="#fff"/><path d="M4 6l6 5 6-5" fill="none" stroke="var(--blue)" stroke-width="1.2"/></svg>
    <span>dana@brightwaterdental.org</span>
  </div>

  <div class="person">
    <p class="person__name">Dana Whitlock</p>
    <p class="person__role">Production engineer</p>
  </div>

  <div class="contact contact--addr">
    <svg viewBox="0 0 20 20"><rect width="20" height="20" rx="3" fill="var(--blue)"/><path d="M10 4a4 4 0 0 0-4 4c0 3 4 8 4 8s4-5 4-8a4 4 0 0 0-4-4z" fill="#fff"/><circle cx="10" cy="8" r="1.5" fill="var(--blue)"/></svg>
    <span>261 9th Floor Plaza<br>Ridgeline Road KTR</span>
  </div>
  <div class="contact contact--web">
    <svg viewBox="0 0 20 20"><rect width="20" height="20" rx="3" fill="var(--blue)"/><circle cx="10" cy="10" r="5.5" fill="none" stroke="#fff" stroke-width="1.3"/><path d="M4.5 10h11M10 4.5c-2.5 3-2.5 8 0 11M10 4.5c2.5 3 2.5 8 0 11" fill="none" stroke="#fff" stroke-width="1"/></svg>
    <span>www.brightwaterdental.org</span>
  </div>
</section>

</body>
</html>
```